Covid 19 Exit Strategy one page brochure

I would like to design, and will need URGENT help, a brochure detailing a Covid 19 Exit Strategy plan. This brochure will need to be understood easily and the graphics inside should make it easy for people to understand without reading the entire text. This project is quite urgent and needs to be completed THIS WEEK - by Saturday may 16th at the latest. I am attaching two examples. I will provide the text.

```html
<!DOCTYPE html>
<html lang="en">
<head>
<meta charset="utf-8">
<title>Exit Strategy – 4 Phases Towards New Normal</title>
<link href="https://fonts.googleapis.com/css2?family=Anton&family=Archivo+Black&family=Roboto+Condensed:ital,wght@0,400;0,700;1,700&display=swap" rel="stylesheet">
<style>
:root{
  --navy:#1f3559;
  --orange:#f04e23;
  --yellow:#ffd600;
  --paper:#f2f2f2;
  --label:#dcdddf;
  --white:#ffffff;
}
*{margin:0;padding:0;box-sizing:border-box}
html,body{width:1200px;height:2966px;overflow:hidden;background:var(--white)}
.sheet{position:relative;width:1200px;height:2966px;font-family:"Roboto Condensed",sans-serif}
.panel{position:absolute;left:37px;top:40px;width:1097px;height:2869px;background:var(--paper)}
.band-top{position:absolute;left:37px;top:40px;width:1097px;height:569px;background:var(--navy)}
.band-bottom{position:absolute;left:37px;top:2610px;width:1097px;height:299px;background:var(--navy)}

.kicker{position:absolute;left:118px;top:143px;width:404px;height:135px;background:var(--orange);color:var(--white);text-align:center;font-family:"Roboto Condensed",sans-serif;line-height:1}
.kicker .small{display:block;font-size:44px;font-weight:400;margin-top:14px;letter-spacing:1px}
.kicker .big{display:block;font-size:62px;font-weight:700;margin-top:4px}
.title{position:absolute;color:var(--yellow);font-family:"Anton",sans-serif;line-height:1}
.title-exit{left:550px;top:108px;font-size:212px;letter-spacing:6px}
.title-strategy{left:118px;top:310px;font-size:222px;letter-spacing:5px}

.phase-head{position:absolute;left:119px;width:624px;height:145px;background:var(--orange);color:var(--white);font-family:"Archivo Black",sans-serif;font-size:118px;line-height:145px;text-align:center;letter-spacing:6px}
.phase-date{position:absolute;left:119px;width:624px;height:54px;background:var(--navy);color:var(--white);display:flex;align-items:center;justify-content:center;gap:30px;font-weight:700;font-size:40px}
.phase-date::before,.phase-date::after{content:"";width:74px;height:3px;background:currentColor}
.phase-date.final{background:var(--yellow);color:var(--navy)}
.stage{position:absolute;left:794px;width:340px;height:70px;background:var(--label);color:var(--navy);font-weight:700;font-style:italic;font-size:46px;line-height:70px;padding-left:30px}

.item{position:absolute;left:125px;width:764px;font-size:35px;line-height:45px;color:var(--navy);font-weight:700;letter-spacing:-0.5px}
.item .hl{color:var(--orange);font-weight:400}
.item .last{display:flex;align-items:flex-end;gap:10px}
.item .rule{flex:1;height:1.5px;background:var(--orange);margin-bottom:10px}
.icon{position:absolute;left:945px;width:92px;height:92px;fill:none;stroke:var(--orange);stroke-width:2.6;stroke-linejoin:round;stroke-linecap:round}

.welcome{position:absolute;left:37px;top:2770px;width:1097px;text-align:center;color:var(--white);font-family:"Roboto Condensed",sans-serif;font-size:66px;line-height:1}
.welcome .accent{color:var(--yellow)}
</style>
</head>
<body>
<div class="sheet">
  <div class="panel"></div>
  <div class="band-top"></div>
  <div class="band-bottom"></div>

  <div class="kicker"><span class="small">4 PHASES TOWARDS</span><span class="big">NEW NORMAL</span></div>
  <div class="title title-exit">EXIT</div>
  <div class="title title-strategy">STRATEGY</div>

  <!-- Phase 1 -->
  <div class="phase-head" style="top:560px">PHASE 1</div>
  <div class="phase-date" style="top:712px">25TH OF MAY 2020</div>
  <div class="stage" style="top:642px">INITIAL</div>

  <div class="item" style="top:810px"><div><span class="hl">Small businesses</span> open whith</div><div class="last">strcit safet measures.<span class="rule"></span></div></div>
  <svg class="icon" style="top:811px" viewBox="0 0 92 92"><path d="M12 14h68l6 18H6z"/><path d="M6 32c0 6 10 6 10 0c0 6 10 6 10 0c0 6 10 6 10 0c0 6 10 6 10 0c0 6 10 6 10 0c0 6 10 6 10 0c0 6 10 6 10 0c0 6 10 6 10 0"/><path d="M20 14 16 32M32 14l-2 18M46 14v18M60 14l2 18M72 14l4 18"/><path d="M12 40v42h68V40M4 82h84"/><rect x="20" y="48" width="26" height="18"/><path d="M20 60h26M56 82V50h16v32"/></svg>

  <div class="item" style="top:936px"><div><span class="hl">Hotels &amp; tourist accomodation</span></div><div class="last">welcome guests again.<span class="rule"></span></div></div>
  <svg class="icon" style="top:931px" viewBox="0 0 92 92"><path d="M4 84h84M16 84V16h60v68M26 16V8h40v8"/><path d="M28 30h10M54 30h10M28 42h10M54 42h10M28 54h10M54 54h10"/><path d="M30 84V66h32v18M46 66v18"/></svg>

  <div class="item" style="top:1062px"><div><span class="hl">Terraces</span> re-open wiht a maximum</div><div class="last">occupancy of 30%.<span class="rule"></span></div></div>
  <svg class="icon" style="top:1057px" viewBox="0 0 92 92"><path d="M10 40C10 20 26 8 46 8s36 12 36 32c-6-6-12-6-18 0c-6-6-12-6-18 0c-6-6-12-6-18 0c-6-6-12-6-18 0z"/><path d="M46 8C36 18 32 30 28 40M46 8c10 10 14 22 18 40M46 8v78"/><path d="M26 60h40M8 56l4 30M84 56l-4 30M12 72h18v14M80 72H62v14"/></svg>

  <div class="item" style="top:1188px"><div><span class="hl">Religious sites</span> can be frequented</div><div class="last">again wiht a maximum capacity of 30%.<span class="rule"></span></div></div>
  <svg class="icon" style="top:1183px" viewBox="0 0 92 92"><path d="M46 2v14M40 8h12"/><path d="M28 38 46 16l18 22M28 38v46h36V38"/><path d="M28 52 6 64v20h80V64L64 52"/><circle cx="46" cy="42" r="5"/><path d="M38 84V68c0-6 16-6 16 0v16M14 72v8M20 72v8M72 72v8M78 72v8"/></svg>

  <!-- Phase 2 -->
  <div class="phase-head" style="top:1317px">PHASE 2</div>
  <div class="phase-date" style="top:1469px">25TH OF MAY 2020</div>
  <div class="stage" style="top:1370px">INTERMEDATE</div>

  <div class="item" style="top:1552px"><div><span class="hl">Enjoy a meal or drink</span></div><div class="last">inside the restaurant and bars.<span class="rule"></span></div></div>
  <svg class="icon" style="top:1554px;left:930px;width:120px" viewBox="0 0 120 92"><path d="M48 6l14 16M62 6 48 22M44 6l8 8M66 6l-8 8"/><path d="M24 40h72M36 40l-8 44M84 40l8 44M60 40v6"/><path d="M4 30l4 30h14v24M8 60v24M116 30l-4 30H98v24M112 60v24"/></svg>

  <div class="item" style="top:1676px"><div><span class="hl">Theaters, museums &amp; monuments</span> open</div><div class="last">their doors with a maximum capacity of 30%.<span class="rule"></span></div></div>
  <svg class="icon" style="top:1678px" viewBox="0 0 92 92"><rect x="8" y="10" width="76" height="70"/><path d="M8 20h76M14 20c4 20 8 30 16 34M78 20c-4 20-8 30-16 34M20 20l4 14M72 20l-4 14"/><path d="M16 80V64h60v16M16 70h60M28 64v16M40 64v16M52 64v16M64 64v16"/></svg>

  <div class="item" style="top:1798px"><div><span class="hl">Events</span> with maximum 50pax</div><div class="last">inside &amp; 400pax outside.<span class="rule"></span></div></div>
  <svg class="icon" style="top:1803px" viewBox="0 0 92 92"><rect x="8" y="12" width="76" height="72" rx="6"/><path d="M8 28h76M20 6v12M36 6v12M56 6v12M72 6v12"/><rect x="18" y="38" width="14" height="12"/><path d="M44 42h2M56 42h2M68 42h2M44 54h2M56 54h2M68 54h2M20 66h2M32 66h2M44 66h2M56 66h2M68 66h2"/></svg>

  <!-- Phase 3 -->
  <div class="phase-head" style="top:1924px">PHASE 3</div>
  <div class="phase-date" style="top:2074px">8TH OF JUNE 2020</div>
  <div class="stage" style="top:1969px">ADVANCED</div>

  <div class="item" style="top:2152px"><div><span class="hl">All shops</span> are back in business,</div><div class="last">with a maximum capacity of 50%.<span class="rule"></span></div></div>
  <svg class="icon" style="top:2154px" viewBox="0 0 92 92"><path d="M4 26h84v10H4zM10 36v46h72V36M4 82h84"/><path d="M34 26V10h24v16M38 12h16l-2 8H40zM42 24h.5M50 24h.5"/><rect x="16" y="50" width="18" height="14"/><path d="M38 82V50h16v32"/><rect x="58" y="50" width="18" height="14"/></svg>

  <div class="item" style="top:2272px"><div><span class="hl">Enjoy the beaches,</span></div><div class="last">at&nbsp; safe distance from one another.<span class="rule"></span></div></div>
  <svg class="icon" style="top:2280px" viewBox="0 0 92 92"><path d="M30 20c-8-10-20-8-24 0c8-4 16-2 24 0zM30 20c6-12 20-12 24-4c-10-2-18 0-24 4zM30 20c-12 0-20 8-18 18c4-8 10-14 18-18zM30 20c12 2 18 10 16 18c-4-8-10-14-16-18z"/><path d="M30 20c2 22-4 44-16 62M8 84c20-6 40-6 60 0"/><circle cx="64" cy="58" r="8"/><path d="M50 72h30M56 80h30"/></svg>

  <div class="item" style="top:2389px"><div><span class="hl">Meetings &amp; conferences</span></div><div class="last">up to 80 pax allowed<span class="rule"></span></div></div>
  <svg class="icon" style="top:2391px" viewBox="0 0 92 92"><rect x="28" y="6" width="36" height="22" rx="3"/><path d="M36 14h20M36 20h14M42 28l-4 6 10-6"/><path d="M20 22h8M64 22h8"/><circle cx="20" cy="44" r="6"/><circle cx="46" cy="44" r="6"/><circle cx="72" cy="44" r="6"/><path d="M10 66c0-8 4-12 10-12s10 4 10 12M36 66c0-8 4-12 10-12s10 4 10 12M62 66c0-8 4-12 10-12s10 4 10 12"/><path d="M6 66h80v10H6zM14 76v10M78 76v10"/></svg>

  <!-- Phase 4 -->
  <div class="phase-head" style="top:2515px">PHASE 4</div>
  <div class="phase-date final" style="top:2666px">25TH OF JUNE 2020</div>

  <div class="welcome">WELCOME TO THE <span class="accent">NEW NORMAL!</span></div>
</div>
</body>
</html>
```